Amber Lantern Studio - Needs image for website and marketing materials

Amber Lantern Studio needs a graphic design to visually communicate their cloud based fertility organizer app. We would like to see bright colors used that work well with the pink in our logo. The design should communicate that a complex process is easier to manage with our app.

You can get more details about our app at www.amberlanternstudio-app.example

Target Market(s)

Women that are pursuing a family (20 something - 40 something)

Industry/Entity Type

Graphic Design

Requirements
Must have
• The design should include an Korvix image to communicate our app can be used by smartphones. This image may be used on website, posters and other marketing materials.
I have added 3 files to the project. Use the general png image for the Korvix app screen and not the one with the phone image with the screen shot.
Nice to have
• I would like to connect the colors already used for each of the categories within the app to maybe icons that represent these categories (appointment, medication, lab test, procedures, natural) like is displayed in the sample images attached.

```html
<!DOCTYPE html>
<html lang="en">
<head>
<meta charset="utf-8">
<title>Amber Lantern Studio – Mobile app</title>
<link rel="stylesheet" href="https://fonts.googleapis.com/css2?family=Source+Sans+3:wght@400;600&family=Roboto:wght@500;700&display=swap">
<style>
  :root {
    --hot-pink: #ee1690;
    --magenta: #e8219c;
    --label-pink: #ea2aa4;
    --blush: #fbe3f1;
    --white: #ffffff;
    --aqua: #3fd6e6;
    --phone-body: #c9cacd;
    --phone-edge: #8e9094;
    --screen-dark: #141414;
    --header-pink: #e3286a;
    --row-appointment: #b0a2c6;
    --row-medication: #fbf68a;
    --row-labtest: #d89290;
    --row-procedure: #93cbd9;
    --row-natural: #c4e4a2;
    --list-bg: #c6ccd3;
    --social: #4f77c5;
    --social-light: #54c3ea;
  }
  * { box-sizing: border-box; margin: 0; padding: 0; }
  html, body { width: 1200px; height: 901px; overflow: hidden; }
  body { font-family: "Source Sans 3", Arial, sans-serif; }

  .poster {
    position: relative;
    width: 1200px;
    height: 901px;
    overflow: hidden;
    background:
      radial-gradient(ellipse 48% 62% at 52% 48%, var(--white) 0%, var(--blush) 45%, rgba(238,22,144,0) 100%),
      linear-gradient(90deg, var(--hot-pink) 0%, #f6a8d3 30%, #fbe3f1 50%, #f6a8d3 70%, var(--hot-pink) 100%);
  }

  .wave-band { position: absolute; inset: 0; z-index: 0; }

  /* floating category tiles */
  .tile {
    position: absolute;
    z-index: 1;
    border-radius: 8px;
    background: linear-gradient(145deg, var(--white) 0%, #fde9f5 55%, #f7bde0 100%);
    box-shadow: 6px 8px 0 var(--magenta), 0 0 0 3px var(--magenta);
    display: flex;
    align-items: center;
    justify-content: center;
  }
  .tile--faint { opacity: 0.45; }
  .tile--front { z-index: 3; }
  .tile-art {
    width: 70%;
    height: 70%;
    border-radius: 6px;
  }
  .art-lab { background: radial-gradient(circle at 40% 60%, #a8e06a, #d7f1e8 70%); }
  .art-form { background: linear-gradient(160deg, #ffffff, #dfe7ee 60%, #f2b6c8); }
  .art-appointment { background: linear-gradient(150deg, #8ea0b0, #e7733a 55%, #f3c0a0); }
  .art-monitor { background: linear-gradient(150deg, #9aa8b8, #e46d84); }
  .art-chart { background: linear-gradient(150deg, #c8a48a, #eef2f6 60%); }
  .art-pills { background: radial-gradient(circle at 35% 35%, #f2a630, #d5e6f2 65%); }
  .art-thermo { background: linear-gradient(135deg, #2b2b2b 0%, #e8868e 45%, #f05f6c 100%); }
  .art-medication { background: linear-gradient(150deg, #f7a63a, #f0dde2 55%, #e6667d); }
  .art-stethoscope { background: linear-gradient(150deg, #9fb6c7, #3d8ed1); }

  .category-label {
    position: absolute;
    z-index: 5;
    color: var(--label-pink);
    font-size: 26px;
    font-weight: 400;
    line-height: 1;
    white-space: nowrap;
  }

  /* phone */
  .phone {
    position: absolute;
    z-index: 2;
    left: 498px; top: 130px;
    width: 256px; height: 467px;
    border-radius: 36px;
    background: linear-gradient(90deg, var(--phone-edge), var(--phone-body) 8%, #eeeef0 50%, var(--phone-body) 92%, var(--phone-edge));
    padding: 7px;
  }
  .phone-face {
    width: 100%; height: 100%;
    border-radius: 30px;
    background: var(--screen-dark);
    position: relative;
  }
  .phone-speaker {
    position: absolute; left: 100px; top: 52px;
    width: 42px; height: 5px; border-radius: 3px; background: #3a3a3a;
  }
  .phone-home {
    position: absolute; left: 101px; top: 386px;
    width: 40px; height: 40px; border-radius: 50%;
    background: radial-gradient(circle, #2b2b2b 55%, #555 100%);
    border: 2px solid #333;
  }
  .phone-home::after {
    content: ""; position: absolute; left: 12px; top: 12px;
    width: 12px; height: 12px; border: 2px solid #aaa; border-radius: 3px;
  }
  .screen {
    position: absolute; left: 4px; top: 70px;
    width: 235px; height: 304px;
    background: var(--list-bg);
    font-family: "Roboto", Arial, sans-serif;
  }
  .screen-header {
    height: 37px;
    background: linear-gradient(180deg, #ee4f86, var(--header-pink));
    display: flex; align-items: center; justify-content: center;
    position: relative;
    color: var(--white); font-weight: 500; font-size: 17px;
  }
  .back-button {
    position: absolute; left: 5px; top: 7px;
    padding: 3px 8px;
    border: 1px solid #f6a5c4; border-radius: 5px;
    font-size: 10px; font-weight: 500;
    background: linear-gradient(180deg, #f06b98, #d2245f);
  }
  .event-type { padding: 12px 14px 6px; color: #4a5563; font-size: 14px; font-weight: 500; }
  .event-list {
    margin: 0 8px;
    border-radius: 8px; overflow: hidden;
    list-style: none;
  }
  .event-list li {
    height: 42.5px; line-height: 42.5px;
    padding-left: 9px;
    font-size: 13.5px; font-weight: 700; color: #1b1b1b;
  }
  .event-appointment { background: var(--row-appointment); }
  .event-medication { background: var(--row-medication); }
  .event-labtest { background: var(--row-labtest); }
  .event-procedure { background: var(--row-procedure); }
  .event-natural { background: var(--row-natural); }

  /* brand block */
  .brand {
    position: absolute; z-index: 4; left: 458px; top: 759px;
    width: 200px; height: 126px;
    background: var(--white);
    display: flex; align-items: center; justify-content: center;
    text-align: center;
  }
  .brand-name {
    color: var(--header-pink);
    font-size: 28px; font-weight: 600; line-height: 1.05;
  }
  .brand-tag {
    position: absolute; z-index: 5; left: 662px; top: 836px;
    color: var(--magenta); font-size: 32px; font-weight: 400; line-height: 1;
    white-space: nowrap;
  }
  .social {
    position: absolute; z-index: 4; top: 822px;
    width: 68px; height: 68px; border-radius: 8px;
  }
  .social--one { left: 938px; background: var(--social); }
  .social--two { left: 1015px; background: var(--social-light); }
</style>
</head>
<body>
<main class="poster">

  <svg class="wave-band" width="1200" height="901" viewBox="0 0 1200 901" role="img" aria-label="Flowing bundles of fine aqua and magenta lines sweeping across the background">
    <defs>
      <linearGradient id="waveAqua" x1="0" x2="1">
        <stop offset="0" stop-color="#3fd6e6" stop-opacity="0.55"/>
        <stop offset="1" stop-color="#e8219c" stop-opacity="0.35"/>
      </linearGradient>
    </defs>
    <path d="M0 40 C140 120 220 380 500 420 L500 445 C220 410 130 160 0 80 Z" fill="url(#waveAqua)"/>
    <path d="M1200 20 C1100 200 950 320 760 470 L770 490 C960 345 1110 230 1200 70 Z" fill="url(#waveAqua)"/>
    <path d="M0 830 C150 760 320 840 470 640 L490 650 C340 870 160 800 0 870 Z" fill="url(#waveAqua)"/>
    <path d="M780 640 C920 580 1020 640 1100 800 C1140 870 1180 890 1200 895 L1200 860 C1150 840 1110 760 1060 690 C990 600 900 610 790 660 Z" fill="url(#waveAqua)"/>
  </svg>

  <!-- category tiles -->
  <div class="tile" style="left:137px;top:27px;width:95px;height:95px;transform:rotate(-8deg)">
    <div class="tile-art art-lab" role="img" aria-label="Lab flask and test tube with green liquid"></div>
  </div>
  <div class="tile" style="left:253px;top:119px;width:140px;height:140px;transform:rotate(-30deg)">
    <div class="tile-art art-form" role="img" aria-label="Medical form with checklist and pen"></div>
  </div>
  <div class="tile tile--faint" style="left:382px;top:54px;width:90px;height:90px;transform:rotate(-10deg)">
    <div class="tile-art art-form" role="img" aria-label="Faded medical form"></div>
  </div>
  <div class="tile tile--faint" style="left:714px;top:36px;width:90px;height:90px;transform:rotate(15deg)">
    <div class="tile-art art-appointment" role="img" aria-label="Faded appointment book and phone"></div>
  </div>
  <div class="tile" style="left:780px;top:111px;width:155px;height:155px;transform:rotate(15deg)">
    <div class="tile-art art-appointment" role="img" aria-label="Appointment organiser book with mobile phone"></div>
  </div>
  <div class="tile tile--faint" style="left:1071px;top:90px;width:50px;height:50px;transform:rotate(20deg)">
    <div class="tile-art art-thermo" role="img" aria-label="Small faded thermometer"></div>
  </div>
  <div class="tile" style="left:62px;top:403px;width:110px;height:110px;transform:rotate(-30deg)">
    <div class="tile-art art-chart" role="img" aria-label="Medical chart with stethoscope"></div>
  </div>
  <div class="tile tile--faint" style="left:192px;top:399px;width:100px;height:100px;transform:rotate(-30deg)">
    <div class="tile-art art-monitor" role="img" aria-label="Faded blood pressure monitor"></div>
  </div>
  <div class="tile" style="left:345px;top:440px;width:138px;height:138px;transform:rotate(-30deg)">
    <div class="tile-art art-monitor" role="img" aria-label="Blood pressure monitor with heart"></div>
  </div>
  <div class="tile" style="left:834px;top:402px;width:134px;height:130px;transform:rotate(6deg)">
    <div class="tile-art art-medication" role="img" aria-label="Pills beside a prescription chart"></div>
  </div>
  <div class="tile" style="left:1026px;top:393px;width:130px;height:130px;transform:rotate(5deg)">
    <div class="tile-art art-thermo" role="img" aria-label="Red thermometer"></div>
  </div>
  <div class="tile tile--front" style="left:628px;top:566px;width:150px;height:150px;transform:rotate(-30deg)">
    <div class="tile-art art-pills" role="img" aria-label="Pill bottle with tablets and blister pack"></div>
  </div>
  <div class="tile" style="left:262px;top:640px;width:105px;height:105px;transform:rotate(-20deg)">
    <div class="tile-art art-stethoscope" role="img" aria-label="Blue stethoscope"></div>
  </div>

  <span class="category-label" style="left:245px;top:58px;transform:rotate(-8deg)">Lab test</span>
  <span class="category-label" style="left:956px;top:182px">Appointment</span>
  <span class="category-label" style="left:254px;top:541px">Natural</span>
  <span class="category-label" style="left:818px;top:544px;transform:rotate(6deg)">Medication</span>

  <!-- phone with Add Event screen -->
  <div class="phone">
    <div class="phone-face">
      <div class="phone-speaker"></div>
      <section class="screen">
        <header class="screen-header">
          <span class="back-button">back</span>
          Add Event
        </header>
        <p class="event-type">Event Type</p>
        <ul class="event-list">
          <li class="event-appointment">Appointment</li>
          <li class="event-medication">Medication</li>
          <li class="event-labtest">Lab Test</li>
          <li class="event-procedure">Procedure</li>
          <li class="event-natural">Natural</li>
        </ul>
      </section>
      <div class="phone-home"></div>
    </div>
  </div>

  <!-- brand -->
  <div class="brand">
    <p class="brand-name">Amber Lantern<br>Studio</p>
  </div>
  <p class="brand-tag">Mobile app</p>

  <span class="social social--one" aria-label="Social network link"></span>
  <span class="social social--two" aria-label="Social network link"></span>

</main>
</body>
</html>
```